Web Design Project for a new download application :-)

We need a website design and a logo design for a new website and desktop application.
The Website will be www.Fetchora.com
The installed application will be: Fetchora

Fetchora is a desktop application that searches and finds all kind of Media files (Movies, Games, Songs, software, etc..)
Fetchora will also manage the download process for the selected files.
Fetchora automates the whole search and download process.

User Flow:
users will initially visit the website.
user will download the application from the website
user will install the application on his computer.
user will run and use the application.

What makes our software special:
-Great search engine for searching media files.
-Very high speed downloads. maximum speeds.
-Allow used to Search by: file type, size, date, format
-Pause and resume downloads
-Get any file you want instantly.
-Unlimited Downloads.

We will need:
Logo
WebSite Design
Icons for the desktop application.

we need only PSDs - no codded pages are needed !

Design to the following screen Size & resolution: 1024 x 768

Target Market(s)

movies and music lovers.
users who download movies, games, softwares, music etc...

Industry/Entity Type

Software

Requirements
Must have
• must have download button

```html
<!DOCTYPE html>
<html lang="en">
<head>
<meta charset="utf-8">
<title>Fetchora — desktop media search and download</title>
<link rel="stylesheet" href="https://fonts.googleapis.com/css2?family=Ubuntu:ital,wght@0,400;0,500;0,700;1,400&family=Arimo:wght@400;700&family=Roboto+Slab:wght@700&display=swap">
<style>
  :root {
    --nav-top: #4f86c8;
    --nav-bottom: #2f64ab;
    --nav-active: #27a0dc;
    --sky-top: #d9ecfb;
    --sky-mid: #eef6fd;
    --ink-blue: #1b5bb0;
    --heading-blue: #0c4aa3;
    --text-grey: #5a5a5a;
    --body-grey: #6b6b6b;
    --green-top: #5cc420;
    --green-bottom: #2f8d0a;
    --footer-bg: #000000;
    --footer-text: #9a9a9a;
    --accent-blue: #2a9ee0;
  }
  * { box-sizing: border-box; margin: 0; padding: 0; }
  html, body { width: 1200px; height: 960px; overflow: hidden; background: #ffffff; }
  body { position: relative; font-family: "Arimo", Arial, sans-serif; }

  .hero {
    position: absolute; left: 0; top: 0; width: 1200px; height: 474px;
    background: linear-gradient(180deg, var(--sky-top) 0%, var(--sky-mid) 55%, #ffffff 85%, #e9e9e9 100%);
    border-bottom: 1px solid #dcdcdc;
  }

  .site-header {
    position: absolute; left: 120px; top: 0; width: 960px; height: 57px; z-index: 3;
    background: linear-gradient(180deg, var(--nav-top), var(--nav-bottom));
    border-radius: 0 0 4px 4px;
    box-shadow: 0 2px 4px rgba(0,0,0,0.25);
  }
  .brand {
    position: absolute; left: 28px; top: 10px;
    font-family: "Ubuntu", sans-serif; font-weight: 500; font-size: 31px; color: #ffffff;
  }
  .main-nav { position: absolute; left: 208px; top: 0; display: flex; height: 57px; }
  .main-nav a {
    display: block; padding: 0 18px; line-height: 57px;
    font-family: "Arimo", sans-serif; font-weight: 700; font-size: 13px; color: #ffffff; text-decoration: none;
  }
  .main-nav a.is-active { background: var(--nav-active); }
  .lang-select {
    position: absolute; left: 768px; top: 14px; width: 165px; height: 28px;
    background: #2b5a9a; border: 1px solid #244f8a;
    font-size: 12px; color: #dfe9f6; line-height: 26px; padding-left: 30px;
  }
  .lang-select .flag { position: absolute; left: 7px; top: 9px; width: 15px; height: 10px; background: #c8d6ea; }
  .lang-select .caret {
    position: absolute; right: 0; top: 0; width: 19px; height: 26px; background: #3f8ad1;
  }
  .lang-select .caret::after {
    content: ""; position: absolute; left: 5px; top: 11px;
    border-left: 5px solid transparent; border-right: 5px solid transparent; border-top: 5px solid #ffffff;
  }

  .hero-copy { position: absolute; left: 0; top: 0; z-index: 2; }
  .hero-title {
    position: absolute; left: 167px; top: 136px; white-space: nowrap;
    font-family: "Ubuntu", sans-serif; font-weight: 400; font-size: 23px; color: var(--text-grey);
  }
  .hero-title .name { color: var(--ink-blue); }
  .feature-ticks { position: absolute; left: 139px; top: 184px; list-style: none; white-space: nowrap; }
  .feature-ticks li {
    position: relative; padding-left: 28px; height: 34px;
    font-family: "Ubuntu", sans-serif; font-size: 17px; color: var(--text-grey);
  }
  .feature-ticks li svg { position: absolute; left: 0; top: -1px; }
  .feature-ticks em { font-style: italic; }

  .download-button {
    position: absolute; left: 168px; top: 315px; width: 281px; height: 93px; z-index: 2;
    border-radius: 12px; border: 3px solid #d7d7d7;
    background: linear-gradient(180deg, var(--green-top), var(--green-bottom));
    box-shadow: 0 6px 10px rgba(0,0,0,0.18);
    color: #ffffff; text-decoration: none;
  }
  .download-button .label {
    position: absolute; left: 22px; top: 14px;
    font-family: "Roboto Slab", serif; font-weight: 700; font-size: 26px; letter-spacing: 0.3px;
  }
  .download-button .sub {
    position: absolute; left: 24px; top: 51px; font-size: 10.5px; line-height: 14px;
  }
  .download-button svg { position: absolute; right: 18px; top: -6px; }

  .hero-art {
    position: absolute; left: 610px; top: 84px; width: 496px; height: 356px; z-index: 1;
    border-radius: 40% 40% 20% 20%;
    background: radial-gradient(ellipse at 55% 55%, #e6c59a 0%, #f3d9c0 25%, #e9f0fa 55%, rgba(238,246,253,0) 72%);
  }
  .slider-dots { position: absolute; left: 554px; top: 441px; display: flex; gap: 5.5px; z-index: 2; }
  .slider-dots span {
    width: 14px; height: 14px; border-radius: 50%;
    background: radial-gradient(circle at 40% 35%, #c9c9c9, #8d8d8d);
  }
  .slider-dots span.is-current { background: radial-gradient(circle at 40% 35%, #b9e45a, #5a9c12); }

  .features { position: absolute; left: 0; top: 474px; width: 1200px; height: 395px; }
  .feature { position: absolute; top: 0; width: 260px; }
  .feature .icon {
    position: absolute; top: 46px; left: 10px; width: 185px; height: 155px;
    border-radius: 20px;
    background: radial-gradient(ellipse at 50% 50%, #c9d9ea 0%, #e7eef6 55%, rgba(255,255,255,0) 75%);
  }
  .feature h2 {
    position: absolute; top: 217px; left: 0; width: 260px;
    font-family: "Arimo", sans-serif; font-weight: 400; font-size: 19px; line-height: 22.5px; color: var(--heading-blue);
  }
  .feature p {
    position: absolute; top: 271px; left: 0; width: 250px;
    font-size: 12.5px; line-height: 22.5px; color: var(--body-grey);
  }
  .feature-divider {
    position: absolute; top: 50px; width: 6px; height: 300px;
    background: linear-gradient(90deg, rgba(0,0,0,0.05), rgba(0,0,0,0));
  }
  .carousel-arrow { position: absolute; top: 178px; }

  .site-footer {
    position: absolute; left: 120px; top: 869px; width: 961px; height: 91px;
    background: var(--footer-bg);
    box-shadow: -20px 10px 30px rgba(0,0,0,0.25), 20px 10px 30px rgba(0,0,0,0.25);
  }
  .site-footer .fold { position: absolute; right: 0; top: 0; }
  .footer-links { position: absolute; left: 68px; top: 27px; font-size: 12.5px; color: var(--footer-text); white-space: nowrap; }
  .footer-links a { color: var(--footer-text); text-decoration: none; }
  .footer-links .sep { margin: 0 5px; }
  .copyright { position: absolute; left: 68px; top: 50px; font-size: 12.5px; color: var(--footer-text); }
  .copyright a { color: var(--accent-blue); text-decoration: none; }
</style>
</head>
<body>

<section class="hero">
  <header class="site-header">
    <div class="brand">Fetchora</div>
    <nav class="main-nav">
      <a href="#" class="is-active">HOME</a>
      <a href="#">DOWNLOAD</a>
      <a href="#">SUPPORT</a>
      <a href="#">AFFILIATES</a>
    </nav>
    <div class="lang-select"><span class="flag"></span>English<span class="caret"></span></div>
  </header>

  <div class="hero-art" role="img" aria-label="Illustration of an open cardboard box bursting with media discs and film reels under a rainbow, with clouds and music notes"></div>

  <div class="hero-copy">
    <h1 class="hero-title"><span class="name">Fetchora</span> is a desktop application that</h1>
    <ul class="feature-ticks">
      <li><svg width="20" height="20" viewBox="0 0 20 20"><path d="M2 11 L7 17 L18 3" fill="none" stroke="#7cb342" stroke-width="2.5" stroke-linecap="round"/></svg><em>searches</em> and <em>finds</em> all kind of Media files</li>
      <li><svg width="20" height="20" viewBox="0 0 20 20"><path d="M2 11 L7 17 L18 3" fill="none" stroke="#7cb342" stroke-width="2.5" stroke-linecap="round"/></svg><em>manages</em> the download process for the selected files</li>
      <li><svg width="20" height="20" viewBox="0 0 20 20"><path d="M2 11 L7 17 L18 3" fill="none" stroke="#7cb342" stroke-width="2.5" stroke-linecap="round"/></svg><em>automates</em> the whole search and download process</li>
    </ul>
  </div>

  <a class="download-button" href="#">
    <span class="label">DOWNLOAD</span>
    <span class="sub">Download Fetchora Application and<br>install it on your desktop</span>
    <svg width="56" height="82" viewBox="0 0 56 82">
      <path d="M4 0 H52 V56 L28 80 L4 56 Z" fill="#f4f4f4" stroke="#d0d0d0"/>
      <path d="M21 18 H35 V44 H45 L28 64 L11 44 H21 Z" fill="#3aa012"/>
    </svg>
  </a>

  <div class="slider-dots">
    <span class="is-current"></span><span></span><span></span><span></span><span></span>
  </div>
</section>

<section class="features">
  <svg class="carousel-arrow" style="left:78px" width="26" height="30" viewBox="0 0 26 30"><path d="M20 2 L5 15 L20 28" fill="none" stroke="#9a9a9a" stroke-width="4"/></svg>

  <article class="feature" style="left:167px">
    <div class="icon" role="img" aria-label="Icon of a film reel and magnifying glass on an open book"></div>
    <h2>Great search engine for searching media files</h2>
    <p>Lorem ipsum dolor sit amet, consectetur adipiscing elit. Etiam auctor tortor tellus, ut consectetur arcu.</p>
  </article>
  <div class="feature-divider" style="left:438px"></div>

  <article class="feature" style="left:488px">
    <div class="icon" role="img" aria-label="Icon of a green download arrow over a globe and hard drive"></div>
    <h2>Very high speed downloads. maximum speeds.</h2>
    <p>Lorem ipsum dolor sit amet, consectetur adipiscing elit. Etiam auctor tortor tellus, ut consectetur arcu.</p>
  </article>
  <div class="feature-divider" style="left:759px"></div>

  <article class="feature" style="left:809px">
    <div class="icon" role="img" aria-label="Icon of documents, a disc, a music note and a magnifying glass"></div>
    <h2>Allow used to Search by file type, size, date, format</h2>
    <p>Lorem ipsum dolor sit amet, consectetur adipiscing elit. Etiam auctor tortor tellus, ut consectetur arcu.</p>
  </article>

  <svg class="carousel-arrow" style="left:1096px" width="26" height="30" viewBox="0 0 26 30"><path d="M6 2 L21 15 L6 28" fill="none" stroke="#9a9a9a" stroke-width="4"/></svg>
</section>

<footer class="site-footer">
  <svg class="fold" width="25" height="25" viewBox="0 0 25 25"><path d="M0 0 H25 V25 Z" fill="#ffffff"/><path d="M0 0 L25 25 H0 Z" fill="#2a9ee0"/></svg>
  <div class="footer-links">
    <a href="#">Home</a><span class="sep">|</span><a href="#">Download</a><span class="sep">|</span><a href="#">Support</a><span class="sep">|</span>
    <a href="#">Affiliates</a><span class="sep">|</span><a href="#">Contact Us</a><span class="sep">|</span><a href="#">Privacy Policy</a><span class="sep">|</span><a href="#">License Agreement</a>
  </div>
  <div class="copyright">Copyright © <a href="#">Fetchora.com</a> 2011.&nbsp; All rights reserved.</div>
</footer>

</body>
</html>
```